Wine Label Design for Ferrant Estate

I need a front and back label for a new wine I am making. I am looking for a classic, elegant and serious wine label. I would like the label to be white with blue and black writing. The blue will be the distinction in the label. The color of blue will be unique and catch the eye. The font of the writing will be unique and could also serve as the brand image for Ferrant Estate. The label can have a design but should be simple and distinct. I envision the paper quality of the label to textured, high quality and add to the overall image of the label.
The label will be timeless. The price of this wine will be $85.00 a bottle, and the label should match a higher priced wine. This wine is family owned and operated.
The writing on the front and back label will be:

FRONT Label-

Ferrant Estate

Howell Mountain

Napa Valley

2022 Cabernet Sauvignon

Back Label-

Cellared and Bottled by Ferrant Estate, Larkmoor, CA 94599

GOVERNMENT WARNING: (1) According to the Surgeon General, women should not drink alcoholic beverages during pregnancy because of the risk of birth defects. (2) Consumption of alcoholic beverages impairs your ability to drive a car or operate machinery, and may cause health problems.

Alc. 14.5% by Vol.

750 ml

Contains Sulfites

```html
<!DOCTYPE html>
<html lang="en">
<head>
<meta charset="utf-8">
<title>Ferrant Estate – 2022 Cabernet Sauvignon Label</title>
<link rel="stylesheet" href="https://fonts.googleapis.com/css2?family=Mulish:wght@200;300;400&display=swap">
<style>
  :root {
    --paper: #ffffff;
    --ink: #111111;
    --muted: #6f6f6f;
    --estate-blue: #05548f;
    --ornament: #e6e6e6;
    --frame: #555555;
    --box-line: #cccccc;
  }
  html, body {
    margin: 0;
    padding: 0;
    width: 1200px;
    height: 1200px;
    overflow: hidden;
    background: var(--paper);
  }
  .canvas {
    position: relative;
    width: 1200px;
    height: 1200px;
    font-family: "Mulish", sans-serif;
    color: var(--ink);
  }
  .label-frame {
    position: absolute;
    left: 347px;
    top: 202px;
    width: 508px;
    height: 794px;
    border: 1px solid var(--frame);
  }
  .border-bands {
    position: absolute;
    left: 0;
    top: 0;
  }
  .brand-mark {
    position: absolute;
    left: 417px;
    top: 289px;
    width: 112px;
    height: 108px;
    border-radius: 50%;
    background: var(--ornament);
  }
  .producer {
    position: absolute;
    left: 510px;
    top: 274px;
    width: 274px;
    text-align: center;
    font-weight: 400;
  }
  .producer-line {
    display: block;
    font-size: 19px;
    line-height: 24px;
  }
  .producer-name {
    display: block;
    font-size: 34px;
    font-weight: 200;
    line-height: 46px;
    margin-top: 1px;
  }
  .producer-town {
    display: block;
    font-size: 18px;
    line-height: 24px;
    margin-top: 0;
  }
  .varietal-band {
    position: absolute;
    left: 399px;
    top: 430px;
    width: 404px;
    height: 76px;
  }
  .varietal-text {
    position: absolute;
    left: 399px;
    top: 439px;
    width: 404px;
    text-align: center;
    color: var(--paper);
    font-weight: 400;
  }
  .vintage {
    display: block;
    font-size: 25px;
    line-height: 30px;
    letter-spacing: 5px;
  }
  .varietal {
    display: block;
    font-size: 25px;
    line-height: 26px;
    letter-spacing: 1.5px;
  }
  .warning {
    position: absolute;
    left: 395px;
    top: 538px;
    width: 262px;
    margin: 0;
    font-size: 20.5px;
    line-height: 21.7px;
    font-weight: 400;
    letter-spacing: -0.3px;
    white-space: nowrap;
  }
  .back-panel {
    position: absolute;
    left: 659px;
    top: 540px;
    width: 152px;
    height: 300px;
    border: 2px solid var(--box-line);
  }
  .volume {
    position: absolute;
    left: 347px;
    width: 508px;
    top: 862px;
    text-align: center;
    font-size: 30px;
    font-weight: 400;
  }
  .facts {
    position: absolute;
    top: 912px;
    font-size: 19px;
    color: var(--muted);
    font-weight: 400;
  }
  .facts-abv { left: 403px; }
  .facts-sulfites { left: 605px; letter-spacing: 0.3px; }
</style>
</head>
<body>
<div class="canvas">
  <div class="label-frame"></div>

  <svg class="border-bands" width="1200" height="1200" viewBox="0 0 1200 1200" role="img" aria-label="Decorative label border area">
    <g fill="var(--ornament)">
      <rect x="371" y="227" width="459" height="31"/>
      <rect x="371" y="942" width="459" height="30"/>
      <rect x="371" y="258" width="6" height="254"/>
      <rect x="824" y="258" width="6" height="254"/>
    </g>
  </svg>

  <div class="brand-mark" aria-hidden="true"></div>

  <div class="producer">
    <span class="producer-line">CELLARED AND BOTTLED</span>
    <span class="producer-line">by</span>
    <span class="producer-name">Ferrant Estate</span>
    <span class="producer-town">Larkmoor, CA 94599</span>
  </div>

  <svg class="varietal-band" width="404" height="76" viewBox="0 0 404 76" aria-hidden="true">
    <path d="M0 0 H404 L398 46 Q394 76 364 76 H40 Q10 76 6 46 Z" fill="var(--estate-blue)"/>
  </svg>
  <div class="varietal-text">
    <span class="vintage">2022</span>
    <span class="varietal">Cabernet Sauvignon</span>
  </div>

  <p class="warning">GOVERNMENT WARNING:<br>(1) According to the<br>Surgeon General,<br>women should not drink<br>alcoholic beverages<br>during pregnancy<br>because of the risk of<br>birth defects.<br>(2) Consumption of<br>alcoholic beverages<br>impairs your ability to<br>drive a car or operate<br>machinery, and may<br>cause health problems.</p>

  <div class="back-panel"></div>

  <div class="volume">750 ml</div>
  <div class="facts facts-abv">Alc. 14.5% by Vol.</div>
  <div class="facts facts-sulfites">CONTAINS SULFITES</div>
</div>
</body>
</html>
```